Meridale Clinical Spa needs an eye-catching poster to help promote our largest sale of spring!

We need a poster that will go on the back of the doors in the patient rooms. Our medical spa is professional and high-end, so we want the poster to look sophisticated, yet very eye-catching.
This project is for our Sunny Soiree special, our second largest sale of the year.

Name: Sunny Soiree
Slogan: Let Your Beauty Bloom
Sale: The More You Buy, The More You Save

Choose from your favorite spa services
VELUNA, Laser Treatments, Microderms, and More!

It would be great to have something blooming. Flowers, or somehow make a woman look like she's blooming.

I am attaching a visual description of our special. However, the poster should NOT include the pricing tiers. I am also attaching our business logo. Thank you!!

Target Market(s)

A majority are women, but some are men. Around 25-55 in age. Middle to upper class who are likely to spend more money.

Industry/Entity Type

Medical

Font styles to use
Sans Serif
Script

Colors

Designer to choose colors to be used in the design.

Requirements
Must have
• Name of promotion: Sunny Soiree
• Slogan: "Let Your Beauty Bloom"
• Concept "The more you buy, the more you save on your favorite spa services"
• Select from your favorite spa services such as VELUNA, laser treatments, microderms, and more!
• Website: MeridaleSpaSpecials.com
• Our logo (attached)
Nice to have
• Modern and creative design. Somehow tying in the "Let your beauty bloom" theme. We don't want the focus to be "The more you buy the more you save"
• We are looking for a unique design that is unlike traditional medical spas in the area that typically include a lot of white and a lot of overly photoshopped images.
• Creativity is key! Something that's different than just text and images. We would be so excited to see that!
Should not have
• Not too much text, but enough to get the point across.

```html
<!DOCTYPE html>
<html lang="en">
<head>
<meta charset="utf-8">
<title>Meridale Clinical Spa – Sunny Soiree Poster</title>
<link href="https://fonts.googleapis.com/css2?family=Open+Sans:wght@300;400;700;800&family=Pinyon+Script&display=swap" rel="stylesheet">
<style>
  :root {
    --page-bg: #2f2f2f;
    --plum-deep: #2a0b2e;
    --plum: #4e1650;
    --violet: #6f2a78;
    --lilac: #b28fd0;
    --lilac-soft: #c8a9e6;
    --white: #ffffff;
    --ink: #222222;
    --accent: #9a63c4;
    --green: #6f8f3a;
  }
  * { box-sizing: border-box; margin: 0; padding: 0; }
  html, body {
    width: 720px; height: 1200px; overflow: hidden;
    background: var(--page-bg);
    font-family: "Open Sans", Arial, sans-serif;
  }
  .poster {
    position: absolute; left: 30px; top: 270px;
    width: 660px; height: 660px; overflow: hidden;
    box-shadow: 0 18px 30px rgba(0,0,0,0.45);
  }
  .flower-photo {
    position: absolute; inset: 0;
    background:
      radial-gradient(ellipse 44% 46% at 50% 47%, var(--lilac-soft) 0%, #9f74c2 55%, rgba(120,60,150,0) 100%),
      radial-gradient(ellipse at 70% 30%, var(--violet) 0%, var(--plum) 55%, var(--plum-deep) 100%);
  }
  .headline {
    position: absolute; left: 0; right: 0; top: 42px;
    text-align: center; color: var(--white);
    font-size: 39px; letter-spacing: 4px; line-height: 1;
  }
  .headline .bold { font-weight: 800; }
  .headline .light { font-weight: 300; }
  .rule {
    position: absolute; left: 73px; width: 493px; height: 1px;
    background: rgba(255,255,255,0.7);
  }
  .rule.top { top: 100px; }
  .rule.bottom { top: 166px; }
  .slogan {
    position: absolute; left: 0; right: 0; top: 108px;
    text-align: center; color: var(--white);
    font-family: "Pinyon Script", cursive;
    font-size: 40px; letter-spacing: 5px; line-height: 1.2;
    white-space: nowrap;
  }
  .offer {
    position: absolute; left: 0; right: 0; top: 237px;
    text-align: center; color: var(--white);
    font-weight: 800; font-size: 40px; letter-spacing: 4px; line-height: 44px;
    text-shadow: 0 2px 6px rgba(0,0,0,0.35);
  }
  .services {
    position: absolute; left: 50px; width: 557px; top: 376px; height: 74px;
    border-radius: 8px; background: rgba(60,20,70,0.45);
    color: var(--white); text-align: center;
  }
  .services .lead { margin-top: 11px; font-size: 20px; font-weight: 300; }
  .services .lead strong { font-weight: 700; }
  .services .list {
    margin-top: 5px; font-family: Arial, sans-serif; font-size: 12.5px; letter-spacing: 0.3px;
  }
  .footer-band { position: absolute; left: 0; top: 0; width: 660px; height: 660px; }
  .brand {
    position: absolute; left: 0; right: 0; top: 547px;
    display: flex; justify-content: center; align-items: center; gap: 9px;
  }
  .brand-dot { width: 22px; height: 22px; border-radius: 50%; background: var(--green); }
  .brand-name { font-size: 32px; font-weight: 400; color: var(--ink); line-height: 1; }
  .brand-sub {
    position: absolute; left: 0; right: 0; top: 586px; padding-left: 52px;
    text-align: center; font-size: 6.5px; font-weight: 700; letter-spacing: 0.4px; color: var(--ink);
  }
  .website {
    position: absolute; left: 0; right: 0; top: 608px;
    text-align: center; font-size: 24px; font-weight: 400; color: var(--ink);
  }
  .website .domain { color: var(--accent); }
</style>
</head>
<body>
  <main class="poster">
    <div class="flower-photo" role="img" aria-label="Close-up photograph of a violet daisy with a yellow centre on a deep plum background"></div>

    <h1 class="headline"><span class="bold">#SUNNY</span> <span class="light">SOIREE</span></h1>
    <div class="rule top"></div>
    <p class="slogan">Let Your Beauty Bloom</p>
    <div class="rule bottom"></div>

    <h2 class="offer">THE MORE YOU BUY<br>THE MORE YOU SAVE</h2>

    <section class="services">
      <p class="lead">CHOOSE FROM <strong>YOUR FAVORITE SPA</strong> SERVICES</p>
      <p class="list">VELUNA,&nbsp; LASER TREATMENTS,&nbsp; MICRODERMS,&nbsp; AND MORE!</p>
    </section>

    <svg class="footer-band" viewBox="0 0 660 660" aria-hidden="true">
      <path d="M0,568 Q330,480 660,568 L660,660 L0,660 Z" fill="var(--lilac)"/>
      <path d="M0,612 Q330,458 660,612 L660,660 L0,660 Z" fill="var(--white)"/>
    </svg>

    <div class="brand">
      <span class="brand-dot"></span>
      <span class="brand-name">Meridale</span>
    </div>
    <p class="brand-sub">MEDICAL CENTER &amp; CLINICAL SPA</p>
    <p class="website">www.<span class="domain">MeridaleSpaSpecials</span>.com</p>
  </main>
</body>
</html>
```